Harborline Energy - needs a business card

Harborline Energy is a U.S. based diesel sourcing and distribution company that supports American oil & gas fields through providing quality product and consistent services.

Target Market(s)

Oil and Gas

Contact Information for Business Card

The background of the card must be white to ensure the logo pops.

Font styles to use
Serif
Sans Serif

Colors

Designer to choose colors to be used in the design.

Requirements
Must have
• Front of Card: Tag line: Harborline Energy, Powering America's Oil & Gas fields.
• Not sure if you guys do this part but just in case...
• Dale Menschow
• Owner/CEO
• C:555.318.4076
• E:Dmenschow@harborlineenergy.example
• W:Harborlineenergy.example
• Locations: Servicing the Powder River, DJ basin and Bakken formations.
• Back of Card: " Frac fueling is what we do. We understand how important diesel fuel is to your operation, which is why our main service line is Frac fueling. We assure our supply and stand by our service"

```html
<!DOCTYPE html>
<html lang="en">
<head>
<meta charset="utf-8">
<title>Harborline Energy – Business Card</title>
<link href="https://fonts.googleapis.com/css2?family=Open+Sans:wght@400;600;700&family=Saira:wght@400;700&display=swap" rel="stylesheet">
<style>
  :root {
    --navy: #0f2d63;
    --red: #c0161f;
    --white: #ffffff;
    --ink: #3a3a3a;
    --rule: #c9c9c9;
    --backdrop: #2a2a2c;
  }
  * { margin: 0; padding: 0; box-sizing: border-box; }
  html, body {
    width: 1200px; height: 1052px; overflow: hidden;
    background: var(--backdrop);
  }
  .canvas { position: relative; width: 1200px; height: 1052px; }
  .card {
    position: absolute; left: 180px; width: 840px; height: 480px;
    background: var(--white); overflow: hidden;
  }
  .card--front { top: 30px; }
  .card--back { top: 542px; }

  /* Front */
  .wave { position: absolute; inset: 0; width: 840px; height: 480px; z-index: 1; }
  .brand {
    position: absolute; left: 62px; top: 120px; width: 280px; z-index: 2;
    display: flex; align-items: center; gap: 14px;
  }
  .brand__dot { width: 30px; height: 30px; border-radius: 50%; background: var(--red); flex: none; }
  .brand__name {
    font-family: "Saira", sans-serif; font-weight: 700; font-size: 30px;
    line-height: 1.05; color: var(--navy); text-transform: uppercase; letter-spacing: 1px;
  }
  .divider {
    position: absolute; left: 362px; top: 84px; width: 1px; height: 210px; background: var(--rule); z-index: 2;
  }
  .details { position: absolute; left: 388px; top: 76px; z-index: 2; }
  .details__name {
    font-family: "Saira", sans-serif; font-weight: 700; font-size: 32px;
    color: var(--navy); letter-spacing: 2px; line-height: 1.1;
  }
  .details__title {
    font-family: "Saira", sans-serif; font-weight: 400; font-size: 21px;
    color: var(--red); letter-spacing: 0.5px; margin-bottom: 14px;
  }
  .details__area {
    font-family: "Open Sans", sans-serif; font-size: 18px; color: var(--ink);
    line-height: 1.3; margin-bottom: 12px;
  }
  .contact { list-style: none; font-family: "Open Sans", sans-serif; font-size: 17px; color: var(--ink); }
  .contact li { display: flex; align-items: center; gap: 10px; line-height: 1.55; }
  .contact svg { width: 15px; height: 15px; flex: none; }
  .tagline {
    position: absolute; right: 36px; bottom: 22px; z-index: 2; text-align: right;
    font-family: "Saira", sans-serif; font-size: 18px; color: var(--white);
    text-transform: uppercase; letter-spacing: 1px; line-height: 1.35;
    white-space: nowrap;
  }

  /* Back */
  .statement {
    position: absolute; left: 90px; right: 90px; top: 170px; text-align: center;
  }
  .statement__head {
    font-family: "Open Sans", sans-serif; font-weight: 700; font-size: 20px;
    color: var(--navy); margin-bottom: 8px;
  }
  .statement__body {
    font-family: "Open Sans", sans-serif; font-size: 18px; color: var(--ink); line-height: 1.45;
  }
</style>
</head>
<body>
<div class="canvas">

  <section class="card card--front">
    <svg class="wave" viewBox="0 0 840 480" aria-hidden="true">
      <path d="M0,250 C150,330 350,360 500,365 C650,370 760,372 840,380 L840,480 L0,480 Z" fill="var(--navy)"/>
      <path d="M0,238 C150,318 350,348 500,353 C650,358 760,360 840,368" fill="none" stroke="var(--red)" stroke-width="4"/>
      <path d="M0,280 C110,332 220,364 380,378 C220,372 110,346 0,296 Z" fill="var(--white)"/>
      <path d="M0,304 C110,352 220,380 360,390 C220,386 110,360 0,309 Z" fill="var(--red)"/>
    </svg>

    <div class="brand">
      <span class="brand__dot"></span>
      <span class="brand__name">Harborline<br>Energy</span>
    </div>

    <div class="divider"></div>

    <div class="details">
      <h1 class="details__name">DALE MENSCHOW</h1>
      <p class="details__title">OWNER/CEO</p>
      <p class="details__area">Servicing the Powder River<br>DJ basin and Bakken formations.</p>
      <ul class="contact">
        <li>
          <svg viewBox="0 0 16 16"><circle cx="8" cy="8" r="7.5" fill="var(--red)"/><path d="M5.2 4.2l1.6-.4.8 2-1 .8c.5 1.1 1.3 1.9 2.4 2.4l.8-1 2 .8-.4 1.6c-3.3.2-6.4-2.9-6.2-6.2z" fill="var(--white)"/></svg>
          <span>555.318.4076</span>
        </li>
        <li>
          <svg viewBox="0 0 16 16"><rect x="1" y="3" width="14" height="10" rx="1.5" fill="var(--red)"/><path d="M2 4.5l6 4.5 6-4.5" fill="none" stroke="var(--white)" stroke-width="1.3"/></svg>
          <span>Dmenschow@harborlineenergy.example</span>
        </li>
        <li>
          <svg viewBox="0 0 16 16"><circle cx="8" cy="8" r="7" fill="var(--red)"/><g fill="none" stroke="var(--white)" stroke-width="1"><ellipse cx="8" cy="8" rx="3" ry="6.5"/><path d="M1.5 8h13M2.5 5h11M2.5 11h11"/></g></svg>
          <span>www.harborlineenergy.example</span>
        </li>
      </ul>
    </div>

    <p class="tagline">Harborline Energy<br>Powering America's Oil &amp; Gas Fields.</p>
  </section>

  <section class="card card--back">
    <div class="statement">
      <h2 class="statement__head">Frac Fueling Is What We Do.</h2>
      <p class="statement__body">We understand how important diesel fuel is to your operation which is why our main service line is Frac fueling. We assure our supply and stand by our service</p>
    </div>
  </section>

</div>
</body>
</html>
```